Tide Harbor Finance Business Cards

Looking for a business card for a new mortgage broking business. Name of the business is Tide Harbor Finance. Purpose of the business is to build trust and strong relationships with clients to then assist them with your mortgage lending needs. Most relationships within the business start off as an enquiry, and then can evolve into a 10+ year relationship, servicing clients from purchasing a new home to then upgrading for their family and even then assisting their children with their first home purchase. Business card should communicate financial security and trust.

Target Market(s)

Targeting professional clients who are looking to build a relationship with a knowledgeable mortgage professional

Industry/Entity Type

Finance - Home Loans

Contact Information for Business Card

Peter Colburn, Director, mobile: 0427 903186, email:peter@tideharborfinance.com.au, website: www.tideharborfinance.com.au

Font styles to use
Sans Serif

Requirements
Must have
• On the front: Must have company logo, contact details as above. On the back: slogan, 'full of choices, free of stress', plus listing services offered: home loans, investment loans, first home buyers, refinancing, car finance

```html
<!DOCTYPE html>
<html lang="en">
<head>
<meta charset="utf-8">
<title>Tide Harbor Finance – Business Cards</title>
<link href="https://fonts.googleapis.com/css2?family=Inter:wght@400;500;700;800&display=swap" rel="stylesheet">
<style>
  :root {
    --backdrop: #959595;
    --navy: #00517a;
    --orange: #f8a332;
    --ink: #333333;
    --white: #ffffff;
  }
  * { margin: 0; padding: 0; box-sizing: border-box; }
  html, body {
    width: 1200px;
    height: 1200px;
    overflow: hidden;
    background: var(--backdrop);
    font-family: "Inter", Arial, sans-serif;
  }
  .card {
    position: absolute;
    left: 179px;
    width: 862px;
    height: 495px;
  }
  .card-front {
    top: 84px;
    background: var(--white);
    display: flex;
    align-items: center;
    justify-content: center;
  }
  .front-wordmark {
    color: var(--navy);
    font-weight: 800;
    font-size: 54px;
    letter-spacing: -0.5px;
  }
  .card-back {
    top: 622px;
    background: var(--navy);
  }
  .brand-tile {
    position: absolute;
    left: 48px;
    top: 109px;
    width: 252px;
    height: 275px;
    background: var(--orange);
    border-radius: 20px;
    display: flex;
    align-items: center;
    padding-left: 20px;
  }
  .tile-wordmark {
    color: var(--ink);
    font-weight: 800;
    font-size: 33px;
    line-height: 1.05;
    width: 200px;
  }
  .contact-block {
    position: absolute;
    left: 330px;
    top: 125px;
    color: var(--orange);
  }
  .person-name {
    font-weight: 700;
    font-size: 32px;
    line-height: 1;
    letter-spacing: 0.5px;
  }
  .person-role {
    margin-top: 9px;
    font-weight: 500;
    font-size: 21px;
    letter-spacing: 2.5px;
  }
  .divider {
    margin-top: 14px;
    width: 357px;
    height: 2px;
    background: var(--orange);
  }
  .contact-list {
    list-style: none;
    margin-top: 28px;
  }
  .contact-item {
    display: flex;
    align-items: center;
    height: 48px;
    font-weight: 500;
    font-size: 21px;
    letter-spacing: 2.6px;
  }
  .contact-icon {
    width: 26px;
    height: 26px;
    margin-right: 12px;
    flex: none;
  }
</style>
</head>
<body>
  <section class="card card-front">
    <div class="front-wordmark">Tide Harbor Finance</div>
  </section>

  <section class="card card-back">
    <div class="brand-tile">
      <div class="tile-wordmark">Tide Harbor Finance</div>
    </div>

    <div class="contact-block">
      <h1 class="person-name">Peter Colburn</h1>
      <p class="person-role">Director</p>
      <div class="divider"></div>
      <ul class="contact-list">
        <li class="contact-item">
          <svg class="contact-icon" viewBox="0 0 24 24" fill="none" stroke="var(--orange)" stroke-width="2" stroke-linecap="round" stroke-linejoin="round">
            <path d="M5 3h4l2 5-2.5 1.5a11 11 0 0 0 6 6L16 13l5 2v4a2 2 0 0 1-2 2A16 16 0 0 1 3 5a2 2 0 0 1 2-2z"/>
            <path d="M15 3a6 6 0 0 1 6 6M15 7a2 2 0 0 1 2 2"/>
          </svg>
          <span>0427 903186</span>
        </li>
        <li class="contact-item">
          <svg class="contact-icon" viewBox="0 0 24 24" fill="var(--orange)">
            <path d="M2 6h20v12H2z"/>
            <path d="M2 6l10 7 10-7M2 18l7-6M22 18l-7-6" stroke="var(--navy)" stroke-width="1.5" fill="none"/>
          </svg>
          <span>peter@tideharborfinance.com.au</span>
        </li>
        <li class="contact-item">
          <svg class="contact-icon" viewBox="0 0 24 24" fill="none" stroke="var(--orange)" stroke-width="2">
            <circle cx="12" cy="12" r="10"/>
            <ellipse cx="12" cy="12" rx="4" ry="10"/>
            <path d="M2 12h20M4 7h16M4 17h16"/>
          </svg>
          <span>www.tideharborfinance.com.au</span>
        </li>
      </ul>
    </div>
  </section>
</body>
</html>
```